Label for LiPo Battery Product for RC Hobby Industry

We need your creativity for a new lithium battery label design. We aim to make our product visually appealing and distinct from competitors. Your design skills are crucial for this task, and we're excited to work with you.
Our main label feature is the colour tag profile, designed to easily identify battery category and power level with a 2-way colour band. Inspired by a tool company that uses a consistent colour profile to identify Phillips head sizing across their range.
The design should be modern, clear, convey speed and suitable for both professional and consumer markets.
Target Market(s)
RC, Drone, Camera community. 20-30 year old.
Industry/Entity Type
Battery, Drone Industry, RC Car
Requirements
Must have
- 2-Way colour tag identity profiling, clear text at 100% scale
Nice to have
- Text and graphic alignment. Comfortable padding and formatting. Colour tag profile, clear text."
Should not have
- Basic, stock looking image.

```html
<!DOCTYPE html>
<html lang="en">
<head>
<meta charset="utf-8">
<title>KAVELT X6240 LiPo Label</title>
<link rel="stylesheet" href="https://fonts.googleapis.com/css2?family=Russo+One&family=Teko:wght@500;600&display=swap">
<style>
  :root {
    --page-bg: #e0e3e6;
    --label-black: #080b10;
    --circuit-deep: #0d1a24;
    --circuit-glow: #123446;
    --brand-red: #b5192e;
    --brand-red-dark: #8e1022;
    --tag-teal: #1f9ba4;
    --tag-teal-dark: #14727a;
    --ink-white: #ffffff;
    --band-white: #f4f4f4;
    --band-grey: #d6d6d6;
    --ink-black: #0b0b0b;
  }
  html, body {
    margin: 0;
    padding: 0;
    width: 1002px;
    height: 1200px;
    overflow: hidden;
    background: var(--page-bg);
  }
  .canvas {
    position: relative;
    width: 1002px;
    height: 1200px;
  }
  .battery-label {
    position: absolute;
    left: 51px;
    top: 358px;
    width: 900px;
    height: 484px;
    display: block;
  }
  .brand-name {
    font-family: "Russo One", sans-serif;
    fill: var(--ink-white);
    font-size: 74px;
    letter-spacing: 4px;
  }
  .model-code {
    font-family: "Russo One", sans-serif;
    font-size: 168px;
    fill: var(--ink-white);
  }
  .spec-tag-text,
  .capacity-text {
    font-family: "Teko", sans-serif;
    font-weight: 600;
    fill: var(--ink-white);
  }
  .spec-tag-text { font-size: 96px; }
  .capacity-text { font-size: 134px; }
  .capacity-text.amp-hours { font-weight: 500; }
  .tagline {
    font-family: "Teko", sans-serif;
    font-weight: 500;
    font-size: 42px;
    fill: var(--ink-black);
    letter-spacing: 0.5px;
  }
</style>
</head>
<body>
<main class="canvas">
  <svg class="battery-label" viewBox="0 0 1278 688" xmlns="http://www.w3.org/2000/svg" aria-label="KAVELT X6240 battery label">
    <defs>
      <linearGradient id="red-panel-fill" x1="0" y1="0" x2="1" y2="0">
        <stop offset="0" stop-color="#c21a31"/>
        <stop offset="0.5" stop-color="var(--brand-red-dark)"/>
        <stop offset="1" stop-color="var(--brand-red)"/>
      </linearGradient>
      <linearGradient id="tagline-band-fill" x1="0" y1="0" x2="1" y2="0">
        <stop offset="0" stop-color="var(--band-white)"/>
        <stop offset="0.6" stop-color="var(--band-grey)"/>
        <stop offset="1" stop-color="var(--band-white)"/>
      </linearGradient>
      <radialGradient id="circuit-fill" cx="0.6" cy="0.3" r="0.8">
        <stop offset="0" stop-color="var(--circuit-glow)"/>
        <stop offset="0.55" stop-color="var(--circuit-deep)"/>
        <stop offset="1" stop-color="var(--label-black)"/>
      </radialGradient>
    </defs>

    <rect class="label-base" x="0" y="0" width="1278" height="688" fill="var(--label-black)"/>
    <rect class="circuit-backdrop" x="300" y="0" width="978" height="545" fill="url(#circuit-fill)" role="img" aria-label="Glowing blue circuit-board trace pattern"/>

    <path class="red-frame" d="M0 0 H230 A80 80 0 0 1 310 80 V543 H1278 V688 H0 Z" fill="url(#red-panel-fill)"/>
    <path class="tagline-band" d="M328 543 H1278 V648 H392 A64 64 0 0 1 328 584 Z" fill="url(#tagline-band-fill)"/>

    <g class="spec-tags">
      <g class="spec-tag">
        <rect x="33" y="118" width="295" height="116" fill="var(--brand-red-dark)"/>
        <rect x="45" y="100" width="295" height="116" fill="var(--tag-teal)"/>
        <polygon points="310,216 340,216 310,236" fill="var(--tag-teal-dark)"/>
        <text class="spec-tag-text" x="80" y="193">120C</text>
      </g>
      <line x1="55" y1="258" x2="290" y2="258" stroke="#d9485a" stroke-width="2"/>
      <g class="spec-tag">
        <rect x="33" y="301" width="295" height="116" fill="var(--brand-red-dark)"/>
        <rect x="45" y="283" width="295" height="116" fill="var(--tag-teal)"/>
        <polygon points="310,399 340,399 310,419" fill="var(--tag-teal-dark)"/>
        <text class="spec-tag-text" x="78" y="376" textLength="215" lengthAdjust="spacingAndGlyphs">6 CELLS</text>
      </g>
      <line x1="55" y1="440" x2="290" y2="440" stroke="#d9485a" stroke-width="2"/>
      <g class="spec-tag">
        <rect x="33" y="483" width="295" height="116" fill="var(--brand-red-dark)"/>
        <rect x="45" y="465" width="295" height="116" fill="var(--tag-teal)"/>
        <polygon points="310,581 340,581 310,601" fill="var(--tag-teal-dark)"/>
        <text class="spec-tag-text" x="78" y="558">22.2V</text>
      </g>
    </g>

    <text class="brand-name" x="855" y="135" text-anchor="middle" textLength="355" lengthAdjust="spacingAndGlyphs">KAVELT</text>

    <text class="model-code" x="470" y="300" textLength="730" lengthAdjust="spacingAndGlyphs">X6240</text>

    <g class="colour-band">
      <polygon class="band-energy" points="395,418 445,347 905,347 860,418 905,490 445,490" fill="var(--brand-red)"/>
      <polygon class="band-capacity" points="872,418 922,347 1278,347 1278,490 922,490" fill="var(--tag-teal)" stroke="var(--label-black)" stroke-width="10" stroke-linejoin="miter"/>
      <text class="capacity-text" x="455" y="466" textLength="365" lengthAdjust="spacingAndGlyphs">1300WH</text>
      <text class="capacity-text amp-hours" x="962" y="466" textLength="240" lengthAdjust="spacingAndGlyphs">1.3Ah</text>
    </g>

    <text class="tagline" x="450" y="612" textLength="760" lengthAdjust="spacingAndGlyphs">PERFORMANCE | ARMOUR PROTECTION | ADVANCED INSULATION</text>
  </svg>
</main>
</body>
</html>
```